Retail brand for customisable denim jackets

Need an interactive website where people can select sizing and colour, as well as a customisable option to add selected patches and/or pins from the inventory to be able to be drag and dropped on various locations on the denim jacket.
Base jackets also available to be bought.

Include online payment options with security.
Contact us button / feedback button

Target Market(s)

Teenagers and young adults but could include adults or others.
Currently not targeted at children.

Industry/Entity Type

Clothing Brand

Coding

Coded - Design and coding required

Number of Pages Required

3 page

Requirements
Must have
• Drag and drop of patches and pins from inventory.

A panel laying out how to order Eg 1) Pick your jacket 2) Choose your patches and pins. 3) Check out your master creation!

Colours: Light Blue, Dark Blue, Black
2d model style with the different faces of the jacket, Eg front view, back view, sleeves, shoulders etc. (for patch and pin placement)
Nice to have
• 3d cgi model of denim jacket for customer to see what their product would look like.

```html
<!DOCTYPE html>
<html lang="en">
<head>
<meta charset="utf-8">
<title>Bluestitch Denim – Customize</title>
<link href="https://fonts.googleapis.com/css2?family=Montserrat:wght@400;500;600;700;800&family=Playfair+Display:wght@700&family=Source+Sans+3:wght@600&display=swap" rel="stylesheet">
<style>
:root{
  --navy:#1c3a78;
  --navy-deep:#1d3358;
  --blue:#2f7bd6;
  --ink:#1b1b1b;
  --muted:#555;
  --line:#d8d8d8;
  --panel:#f2f2f2;
  --footer:#202020;
  --footer-bottom:#131313;
  --footer-text:#b9b9b9;
}
*{margin:0;padding:0;box-sizing:border-box}
html,body{width:726px;height:1200px;overflow:hidden;background:#fff}
body{font-family:'Montserrat',sans-serif;color:var(--ink)}
.page{position:absolute;left:0;top:0;width:1366px;height:2258px;transform:scale(0.53148);transform-origin:0 0}
.abs{position:absolute}

.topbar{left:0;top:0;width:1366px;height:40px;background:var(--navy);color:#fff;font-size:15px;font-weight:500}
.topbar span{position:absolute;top:11px}
.topbar .user{width:20px;height:20px;border:2px solid #fff;border-radius:50%;top:10px;left:1146px}

.header{left:0;top:40px;width:1366px;height:102px;background:#fff}
.brand{left:68px;top:30px;display:flex;align-items:center;gap:12px;font-size:20px;font-weight:700;color:var(--navy-deep)}
.brand i{width:38px;height:38px;border-radius:50%;background:var(--navy-deep);display:block}
.nav a{position:absolute;top:41px;font-size:16.5px;font-weight:600;color:var(--ink);text-decoration:none;letter-spacing:.3px}
.nav a.active{color:var(--blue)}
.nav .bar{position:absolute;left:832px;top:96px;width:79px;height:6px;background:var(--blue)}
.cart-label{left:1220px;top:42px;font-size:16.5px;font-weight:600}

.hero{left:0;top:142px;width:1366px;height:416px;background:linear-gradient(100deg,#e9e6e4 0%,#f4f2f1 30%,#e3dfec 55%,#d8d3df 75%,#ece2d6 100%)}
.hero-card{left:561px;top:222px;width:262px;height:262px;background:var(--navy-deep);border:2px solid #fff;color:#fff;text-align:center}
.hero-card .frame{position:absolute;left:6px;top:6px;right:6px;bottom:6px;border:1px solid rgba(255,255,255,.75)}
.hero-card .l1{position:absolute;top:30px;width:100%;font-size:21px;font-weight:700}
.hero-card .l2{position:absolute;top:62px;width:100%;font-size:58px;font-weight:800;letter-spacing:1px}
.hero-card .l3{position:absolute;top:155px;width:100%;font-size:17px;font-weight:500}
.hero-card .l3:before,.hero-card .l3:after{content:"";position:absolute;top:10px;width:58px;height:1px;background:#fff}
.hero-card .l3:before{left:32px}.hero-card .l3:after{right:32px}
.hero-card .l4{position:absolute;top:190px;width:100%;font-family:'Source Sans 3',sans-serif;font-size:31px;font-weight:600}

.crumb{left:70px;top:590px;font-size:16px;font-weight:500}
.crumb b{color:var(--blue);font-weight:500}

.filters{left:68px;top:638px;width:262px;height:686px;border:1px solid var(--line)}
.filters h3{height:52px;background:var(--panel);border-bottom:1px solid var(--line);font-family:'Playfair Display',serif;font-size:24px;padding:12px 0 0 23px;letter-spacing:.5px}
.fgroup{position:absolute;left:0;width:260px;border-bottom:1px solid var(--line)}
.fgroup .t{position:absolute;left:24px;font-size:18px;font-weight:500}
.fgroup .m{position:absolute;right:20px;font-size:18px;font-weight:700}
.chip{position:absolute;top:56px;height:32px;background:#efefef;font-size:16px;font-weight:500;text-align:center;line-height:32px}
.sw{position:absolute;top:56px;width:24px;height:24px}
.cb{position:absolute;left:24px;width:24px;height:24px;background:#f2f2f2;border:1px solid #ddd}
.cbl{position:absolute;left:60px;font-size:18px;font-weight:500}
.pbox{position:absolute;top:120px;width:98px;height:38px;border:1px solid #c9c9c9;text-align:center;line-height:36px;font-size:18px}

.step{left:383px;top:630px;font-family:'Playfair Display',serif;font-size:40px}
.sub{left:382px;top:688px;font-size:25px;font-weight:500;color:var(--blue);letter-spacing:.3px}
.grid{left:382px;top:744px;width:913px;height:892px;border:1px solid #e6e6e6}
.pimg{border:1px solid #e2e2e2}
.pname{font-size:17px;font-weight:600;color:#333;text-align:center;width:300px}
.price{font-size:30px;font-weight:500;color:var(--blue);text-align:center;width:300px}
.badge{width:58px;height:58px;border-radius:50%;background:var(--blue);color:#fff;font-size:19px;font-weight:700;text-align:center;line-height:58px}
.badge sup{font-size:9px}

.pager a{position:absolute;top:1680px;height:30px;border:1px solid #aaa;font-size:16px;font-weight:500;line-height:28px;text-align:center;color:var(--ink)}
.pager a.word{color:var(--blue)}

.footer{left:0;top:1770px;width:1366px;height:428px;background:var(--footer)}
.fcol h4{position:absolute;font-size:15px;font-weight:600;color:#fff}
.fcol p{position:absolute;font-size:15px;color:var(--footer-text)}
.social{position:absolute;top:1888px;width:47px;height:47px;border-radius:50%;background:#fff}
.news{left:821px;top:1977px;font-size:15px;font-weight:600;color:#fff}
.email{left:823px;top:2023px;width:322px;height:47px;border:1px solid #555;color:#ccc;font-size:15px;padding:13px 0 0 22px}
.subscribe{left:1145px;top:2023px;width:150px;height:47px;background:var(--blue);color:#fff;font-size:15px;font-weight:600;text-align:center;line-height:47px}
.totop{left:1254px;top:2127px;width:38px;height:38px;background:var(--blue)}
.bottom{left:0;top:2198px;width:1366px;height:60px;background:var(--footer-bottom);color:#ccc;font-size:14px;text-align:center;padding-top:24px}
.bottom .rule{position:absolute;left:70px;top:0;width:1225px;height:1px;background:var(--blue)}
</style>
</head>
<body>
<div class="page">

  <div class="abs topbar">
    <span style="left:69px">Welcome to Bluestitch Denim Store!</span>
    <span style="left:505px">COVID-19</span>
    <span style="left:612px">Feedback</span>
    <span style="left:719px">Track Order</span>
    <span style="left:846px">Find Stores &amp; Services</span>
    <span style="left:1048px">Help</span>
    <span class="user"></span>
    <span style="left:1177px">Signin/Register</span>
  </div>

  <header class="abs header">
    <div class="abs brand"><i></i>Bluestitch Denim</div>
    <nav class="nav">
      <a style="left:353px">MEN</a>
      <a style="left:437px">WOMEN</a>
      <a style="left:553px">KIDS</a>
      <a style="left:639px">NEW ARRIVALS</a>
      <a class="active" style="left:820px">CUSTOMIZE</a>
      <a style="left:968px">CONTACT US</a>
      <span class="bar"></span>
    </nav>
    <svg class="abs" style="left:1130px;top:38px" width="26" height="26" viewBox="0 0 26 26" aria-label="Search"><circle cx="10" cy="10" r="8" fill="none" stroke="#2f7bd6" stroke-width="3"/><line x1="16" y1="16" x2="24" y2="24" stroke="#2f7bd6" stroke-width="3.5" stroke-linecap="round"/></svg>
    <svg class="abs" style="left:1186px;top:38px" width="26" height="24" viewBox="0 0 26 24" aria-label="Cart"><path d="M8 8 V5 a5 5 0 0 1 10 0 V8" fill="none" stroke="#2f7bd6" stroke-width="2.5"/><rect x="1" y="8" width="24" height="15" rx="2" fill="#2f7bd6"/></svg>
    <div class="abs cart-label">CART: 2</div>
  </header>

  <section class="abs hero" role="img" aria-label="Tailor working at a sewing machine with spools of coloured thread"></section>
  <div class="abs hero-card">
    <div class="frame"></div>
    <div class="l1">CUSTOMIZE THE</div>
    <div class="l2">DENIM</div>
    <div class="l3">Let`s</div>
    <div class="l4">Try and Enjoy</div>
  </div>

  <div class="abs crumb">Home &gt; <b>Customize</b></div>

  <aside class="abs filters">
    <h3>FILTERS</h3>
    <div class="fgroup" style="top:52px;height:111px">
      <span class="t" style="top:14px">Size</span><span class="m" style="top:10px">-</span>
      <span class="chip" style="left:24px;width:40px">L</span>
      <span class="chip" style="left:76px;width:44px">XL</span>
      <span class="chip" style="left:128px;width:52px">XXL</span>
    </div>
    <div class="fgroup" style="top:163px;height:113px">
      <span class="t" style="top:19px">Color</span><span class="m" style="top:15px">-</span>
      <span class="sw" style="left:24px;background:#f0f0f0;border:1px solid #ddd"></span>
      <span class="sw" style="left:59px;background:#1b1b1b"></span>
      <span class="sw" style="left:95px;background:#3f78c5"></span>
      <span class="sw" style="left:130px;background:#2b3f66"></span>
      <span class="sw" style="left:165px;background:#8fa6ba"></span>
      <span class="sw" style="left:198px;background:#a8680a"></span>
    </div>
    <div class="fgroup" style="top:276px;height:217px">
      <span class="t" style="top:22px">Gender</span><span class="m" style="top:18px">-</span>
      <span class="cb" style="top:78px"></span><span class="cbl" style="top:78px">Men</span>
      <span class="cb" style="top:118px"></span><span class="cbl" style="top:118px">Women</span>
      <span class="cb" style="top:158px"></span><span class="cbl" style="top:158px">Kids</span>
    </div>
    <div style="position:absolute;top:493px;left:0;width:260px;height:190px">
      <span style="position:absolute;left:24px;top:19px;font-size:18px;font-weight:500">Price</span>
      <span style="position:absolute;right:20px;top:15px;font-size:18px;font-weight:700">-</span>
      <svg style="position:absolute;left:20px;top:68px" width="225" height="20" viewBox="0 0 225 20"><line x1="10" y1="10" x2="222" y2="10" stroke="#bbb" stroke-width="2"/><line x1="10" y1="10" x2="142" y2="10" stroke="#2f7bd6" stroke-width="2.5"/><rect x="4" y="4" width="12" height="12" fill="#2f7bd6" transform="rotate(45 10 10)"/><rect x="136" y="4" width="12" height="12" fill="#2f7bd6" transform="rotate(45 142 10)"/></svg>
      <span class="pbox" style="left:22px">$30</span>
      <span style="position:absolute;left:128px;top:125px;font-size:18px;font-weight:700">-</span>
      <span class="pbox" style="left:148px">$250</span>
    </div>
  </aside>

  <h1 class="abs step">Step 1 of 3</h1>
  <h2 class="abs sub">Choose your Product</h2>
  <div class="abs grid"></div>

  <div class="abs pimg" style="left:397px;top:754px;width:284px;height:328px;background:linear-gradient(135deg,#33c4dd,#1aa9cc 60%,#1d3a5a)" role="img" aria-label="Man in a blue denim shirt sitting against a turquoise wall"></div>
  <div class="abs pimg" style="left:697px;top:754px;width:286px;height:328px;background:linear-gradient(160deg,#efefef,#dfe3e8 50%,#8aa4c4)" role="img" aria-label="Woman in a denim jacket working on a laptop"></div>
  <div class="abs pimg" style="left:999px;top:754px;width:285px;height:328px;background:linear-gradient(145deg,#8eb4d6,#6d98c0 55%,#4a4a52)" role="img" aria-label="Light denim jacket laid flat with sunglasses"></div>
  <div class="abs badge" style="left:1014px;top:770px">40<sup>%</sup></div>

  <div class="abs pimg" style="left:397px;top:1204px;width:284px;height:328px;background:linear-gradient(160deg,#f9bf4c,#f5a623 60%,#2b3a5a)" role="img" aria-label="Woman in a dark denim jacket against a yellow background"></div>
  <div class="abs pimg" style="left:697px;top:1204px;width:286px;height:328px;background:linear-gradient(160deg,#f0f0f0,#e4e6ea 55%,#4f79b5)" role="img" aria-label="Girl in a star-print denim jacket"></div>
  <div class="abs pimg" style="left:999px;top:1204px;width:285px;height:328px;background:linear-gradient(170deg,#e8e8e8,#9fb6cc 45%,#2b2b2b 70%,#9ab3cc)" role="img" aria-label="Person wearing an oversized denim jacket over a black tee"></div>
  <div class="abs badge" style="left:1014px;top:1220px">40<sup>%</sup></div>

  <div class="abs pname" style="left:387px;top:1101px">Denim Jacket 2 Dress</div>
  <div class="abs price" style="left:391px;top:1131px">$ 112.50</div>
  <div class="abs pname" style="left:690px;top:1101px">Denim Jacket 3 Dress</div>
  <div class="abs price" style="left:682px;top:1131px">$ 96.00</div>
  <div class="abs pname" style="left:990px;top:1101px">Denim Jacket 4 Dress</div>
  <div class="abs price" style="left:990px;top:1131px">$ 121.19</div>

  <div class="abs pname" style="left:387px;top:1551px">Denim Jacket 2 Dress</div>
  <div class="abs price" style="left:391px;top:1581px">$ 112.50</div>
  <div class="abs pname" style="left:690px;top:1551px">Denim Jacket 3 Dress</div>
  <div class="abs price" style="left:682px;top:1581px">$ 96.00</div>
  <div class="abs pname" style="left:990px;top:1551px">Denim Jacket 4 Dress</div>
  <div class="abs price" style="left:990px;top:1581px">$ 121.19</div>

  <div class="pager">
    <a class="word" style="left:383px;width:64px">Prev</a>
    <a style="left:458px;width:35px">1</a>
    <a style="left:503px;width:35px">2</a>
    <a style="left:548px;width:35px">3</a>
    <a class="word" style="left:592px;width:64px">Next</a>
  </div>

  <footer class="abs footer"></footer>
  <div class="fcol">
    <h4 style="left:78px;top:1828px">SHOPS</h4>
    <p style="left:78px;top:1884px">New In</p>
    <p style="left:78px;top:1912px">Women</p>
    <p style="left:78px;top:1941px">Men</p>
    <p style="left:78px;top:1969px">Kids</p>
    <p style="left:78px;top:1998px">Sale &amp; Special Offers</p>
    <p style="left:78px;top:2026px">Rating</p>

    <h4 style="left:304px;top:1827px">INFORMATION</h4>
    <p style="left:304px;top:1884px">About us</p>
    <p style="left:304px;top:1914px">Customer Service</p>
    <p style="left:304px;top:1944px">New Collection</p>
    <p style="left:304px;top:1974px">Best Sellers</p>
    <p style="left:304px;top:2004px">Privacy policy</p>
    <p style="left:304px;top:2034px">Terms &amp; condition</p>

    <h4 style="left:540px;top:1826px">CUSTOMER SERVICE</h4>
    <p style="left:540px;top:1889px">Orders and Returns</p>
    <p style="left:540px;top:1919px">Contact Us</p>
    <p style="left:540px;top:1949px">Help &amp; FAQs</p>
    <p style="left:540px;top:1979px">Store Locations</p>

    <h4 style="left:820px;top:1826px">STAY CONNECTED</h4>
  </div>
  <span class="social" style="left:823px"></span>
  <span class="social" style="left:887px"></span>
  <span class="social" style="left:950px"></span>
  <span class="social" style="left:1014px"></span>
  <div class="abs news">SUBSCRIBE <i style="font-family:'Playfair Display',serif">in</i> OUR NEWS LETTER</div>
  <div class="abs email">Enter Your Email Address</div>
  <div class="abs subscribe">SUBSCRIBE</div>
  <div class="abs totop"><svg width="38" height="38" viewBox="0 0 38 38" aria-label="Back to top"><polyline points="12,22 19,15 26,22" fill="none" stroke="#fff" stroke-width="2.5"/></svg></div>

  <div class="abs bottom"><span class="rule"></span>Bluestitch Denim© 2020. All Rights Reserved.</div>
  <svg class="abs" style="left:672px;top:2198px" width="22" height="10" viewBox="0 0 22 10"><polygon points="0,0 22,0 11,10" fill="#2f7bd6"/></svg>

</div>
</body>
</html>
```